Flyer Design Project for Brightwater Wellbeing Rooms

We are a psychology clinic that specialises in eating, parenting and chronic illness & pain. See our website for a summary.

We need a flyer that will go to doctors and schools in the local area.

Things to include on the front page:

Immediate appointments available
After hours appointments available
Male and female psychologists

Phone 9563 2190
Web brightwaterwellbeingrooms.com.au

On the back page:

Phone 9563 2190
Suite 1/1287 Marlowe Rd, Kelverton East 3185.
brightwaterwellbeingrooms.com.au

Parenting: Parenthood is an amazing journey, but for lots of people it raises all sorts of issues from fear of birth, breastfeeding difficulties and settling problems, to toddler discipline and food fussiness all the way through to getting help for your depressed or anxious adolescent. Our Parenting Psychologists can help you be the best parent you can be which will in turn lead to happier families, homes, children and parents.

Chronic illness/pain: Diabetes, heart disease, arthritis, asthma, migraines, dizziness, chronic fatigue syndrome, infertility, and PCOS are just some of the conditions that can be managed with psychological interventions. Everything we do is about helping you to manage your condition and get back to focusing on what you really want your life to be about.

Eating: Whether you suffer from anorexia, bulimia or binge eating, our strategies help you develop a healthy relationship with food and your body. The practical tips and strategies that we can provide are very useful for people undergoing lapband surgery or liposuction.

I am interested in whether the photographs that I have already purchased can be used...so please have a look through the website and see which you think will suit your design. Photographs are not absolutely necessary though, so if it doesn't fit with your idea that is okay too.
Updates

HI Everyone,

Thanks for submitting so far! I haven't found anything yet that has hit the mark. And I am thinking that is my fault and maybe that way i have described what I want. I apologise and hope that this update might help.

This brochure is likely to sit with lots of other brochures in a doctors waiting room so it needs to be different - so that it will be noticed.

The majority of our market are women - so something feminine is important. Maybe it needs to be a little more playful that I had initially thought. Like maybe not your standard blocky text and bolds and primary colours. But something more creative, more personal.

I want to not focus just on the family theme. Parenting is one area that we cover, but also we help people with eating disorders and chronic illness/chronic pain. So the photographs that I use need to be more general. It is importnat to focus on happy and healthy looking people. As we went to appeal to what my potential clients want to look like and feel like.

I do hope this helps to guide you. I promise that once I see a flyer that I could choose, I will turn the funding to guaranteed. I did this last time...I am just a bit nervous as I haven't received anything yet that I am excited about.

Kindest regards,

Marnie.

Hi Everyone,

Thank you for your designs coming in! As promised, as soon as I received a design that I could see myself choosing I would change the status from refundable to committed. I have now done this!

I have received a design that I would say is good. It is not perfect however...so please keep the ideas coming.

To give more direction, the one that came in has a nice theme that runs through the brochure. Not too many different types of font and colours detracting from the flow of the flyer. However, the thing that I am concerned about is whether it will stand out enough on a rack of other flyers in a doctors waiting room.

I hope this helps with your creative ideas.

Thanks again to everyone!

Marnie.

Thanks SO much to everyone who is putting in designs. You are making my decision difficult!

I am wondering if you can update your designs with a few things:

can I ask you to make some text changes:

1. Can we have a heading on the front page: Psychologists  and then can you put Kelverton East in smaller writing just below it?

2. Id like to say on the front: Specialising in parenting, disordered eating and chronic pain & illness

3. Delete Male & Female Psychologists

4. In general we dont' need to have the logo standing out. We don't have a well known brand yet, so I am not wanting to take up valuable space with this - so perhaps it shoudl be small and maybe just on the back? Keeping the name of our clinic on the front with the website shoudl be sufficient.

Thanks heaps everyone...I will make decision very soon!

Target Market(s)

20-40 year olds. Working. Educated. Female. They might have a family/children.
Australian. Engish speaking.

Industry/Entity Type

Clinic

Requirements
Must have
• I would like to include our logo. Please do not use the colour green that it is in. I hate that colour! but I LOVE the logo.

I would like to follow through with some of the themes of the website and other stationary.

I will attach some of the other stationary I have had designed.

I really like the colours in the letterhead - especially that blue of the logo.

I think it needs to have a dash of colour with it at least...something that will stand out and be noticed on a brochure rack...but also have a look of class/sophistication/modern.
Nice to have
• Perhaps photograph of happy and healthy people.
Should not have
• I don't like bold text or too many different types of fonts.

It shouldn't look too cluttered so I might need to reduce the text I have included - I will need to see it first.

```html
<!DOCTYPE html>
<html lang="en">
<head>
<meta charset="utf-8">
<title>Brightwater Wellbeing Rooms – Flyer</title>
<link href="https://fonts.googleapis.com/css2?family=Patrick+Hand&family=Open+Sans:wght@400;600&display=swap" rel="stylesheet">
<style>
  :root {
    --backdrop: #5b3a1d;
    --paper: #ffffff;
    --teal: #1d7a80;
    --taupe: #9a8a71;
    --yellow: #f7dc55;
    --soft-yellow: #f4e56b;
    --ink: #4a4a3c;
    --body-ink: #4f4f4f;
    --sq1: #6e9f7c; --sq2: #7fc6c9; --sq3: #6fa5a4; --sq4: #808f94;
    --sq5: #3e7c7b; --sq6: #85c9ca; --sq7: #4b4b4b; --sq8: #8f9a72;
  }
  * { box-sizing: border-box; margin: 0; padding: 0; }
  html, body { width: 1200px; height: 1090px; overflow: hidden; background: var(--backdrop); }
  body { position: relative; font-family: "Open Sans", Arial, sans-serif; }

  .panel { position: absolute; top: 0; height: 1090px; background: var(--paper); overflow: hidden; }
  .front { left: 64px; width: 534px; }
  .back { left: 632px; width: 507px; }

  .swatch-strip { position: absolute; left: 0; right: 0; height: 34px; display: flex; }
  .swatch-strip span { flex: 1; }
  .swatch-strip span:nth-child(1) { background: var(--sq1); }
  .swatch-strip span:nth-child(2) { background: var(--sq2); }
  .swatch-strip span:nth-child(3) { background: var(--sq3); }
  .swatch-strip span:nth-child(4) { background: var(--sq4); }
  .swatch-strip span:nth-child(5) { background: var(--sq5); }
  .swatch-strip span:nth-child(6) { background: var(--sq6); }
  .swatch-strip span:nth-child(7) { background: var(--sq7); }
  .swatch-strip span:nth-child(8) { background: var(--sq8); }
  .strip-top { top: 0; }
  .strip-bottom { bottom: 0; }

  /* front */
  .headline { position: absolute; top: 52px; left: 0; width: 100%; text-align: center;
    font-family: "Patrick Hand", cursive; font-size: 60px; color: var(--ink); letter-spacing: 1px; }
  .hero-photo { position: absolute; top: 169px; left: 0; width: 360px; height: 326px;
    background: linear-gradient(135deg, #c9a27a 0%, #e8d6bd 40%, #b7c08a 75%, #8a9a5a 100%); }
  .service-disc { position: absolute; left: 268px; top: 129px; width: 404px; height: 404px;
    border-radius: 50%; background: var(--taupe); border: 8px solid var(--paper); }
  .service-list { position: absolute; right: 36px; top: 200px; text-align: right;
    font-size: 35px; line-height: 1.15; color: var(--soft-yellow); list-style: none; }
  .service-list li { margin-bottom: 34px; }
  .service-list li.two-line { line-height: 1.15; }

  .perks { position: absolute; left: 36px; top: 538px; list-style: none;
    font-family: "Patrick Hand", cursive; font-size: 36px; color: var(--teal); }
  .perks li { display: flex; align-items: center; height: 60px; }
  .perks svg { width: 26px; height: 26px; margin-right: 16px; }

  .cta-band { position: absolute; top: 765px; left: 150px; right: 0; height: 92px; background: var(--taupe); }
  .cta-band .phone { position: absolute; left: 58px; top: 18px; font-size: 40px; color: var(--paper); }
  .cta-arrow { position: absolute; top: 748px; left: 0; width: 200px; height: 126px; }
  .cta-arrow-text { position: absolute; top: 772px; left: 14px; width: 150px; text-align: center;
    font-size: 20px; line-height: 1.2; color: var(--ink); }

  .clinic-name { position: absolute; top: 905px; left: 0; width: 100%; display: flex;
    justify-content: center; align-items: center; gap: 12px; font-size: 17px; color: var(--teal);
    letter-spacing: 1px; text-transform: uppercase; }
  .clinic-name i { width: 22px; height: 22px; border-radius: 50%; background: var(--sq2); display: block; }

  .web-band { position: absolute; top: 975px; left: 0; width: 100%; height: 60px; background: var(--teal);
    color: var(--yellow); font-size: 23px; text-align: center; line-height: 60px; }

  /* back */
  .faint-ring { position: absolute; left: 150px; top: 160px; width: 420px; height: 420px;
    border-radius: 50%; border: 26px solid rgba(154,138,113,0.16); }
  .topic-head { position: absolute; left: 0; width: 100%; height: 42px; background: var(--teal);
    color: var(--paper); font-size: 27px; font-weight: 600; padding-left: 24px; line-height: 42px; }
  .topic-text { position: absolute; left: 24px; right: 22px; font-size: 16.5px; line-height: 26.5px; color: var(--body-ink); }
  .head-parenting { top: 12px; }
  .text-parenting { top: 68px; }
  .head-chronic { top: 338px; }
  .text-chronic { top: 394px; }
  .head-eating { top: 627px; height: 46px; line-height: 46px; }
  .text-eating { top: 688px; }

  .info-band { position: absolute; top: 872px; left: 110px; right: 0; height: 90px; background: var(--taupe); }
  .info-band .phone { position: absolute; left: 58px; top: 8px; font-size: 40px; color: var(--paper); }
  .info-band .visit { position: absolute; left: 58px; top: 62px; font-size: 14.5px; color: var(--yellow); }
  .info-arrow { position: absolute; top: 862px; left: 0; width: 160px; height: 112px; }
  .info-arrow-text { position: absolute; top: 872px; left: 10px; width: 110px; text-align: center;
    font-size: 24px; line-height: 1.25; color: var(--paper); }
  .address { position: absolute; top: 1016px; left: 0; width: 100%; text-align: center; font-size: 17px; color: var(--ink); }
</style>
</head>
<body>

<section class="panel front">
  <div class="swatch-strip strip-top"><span></span><span></span><span></span><span></span><span></span><span></span><span></span><span></span></div>

  <h1 class="headline">Expert Family Advice</h1>

  <div class="hero-photo" role="img" aria-label="Photo of a smiling mother with her toddler outdoors"></div>
  <div class="service-disc"></div>
  <ul class="service-list">
    <li>Parenting</li>
    <li>Eating</li>
    <li class="two-line">Chronic Pain<br>&amp; Illness</li>
  </ul>

  <ul class="perks">
    <li><svg viewBox="0 0 26 26"><rect x="3" y="3" width="20" height="20" fill="none" stroke="#4a4a3c" stroke-width="2"/><path d="M7 13l4 4 8-9" fill="none" stroke="#4a4a3c" stroke-width="2"/></svg>Immediate appointments</li>
    <li><svg viewBox="0 0 26 26"><rect x="3" y="3" width="20" height="20" fill="none" stroke="#4a4a3c" stroke-width="2"/><path d="M7 13l4 4 8-9" fill="none" stroke="#4a4a3c" stroke-width="2"/></svg>Afterhours appointments</li>
    <li><svg viewBox="0 0 26 26"><rect x="3" y="3" width="20" height="20" fill="none" stroke="#4a4a3c" stroke-width="2"/><path d="M7 13l4 4 8-9" fill="none" stroke="#4a4a3c" stroke-width="2"/></svg>Male &amp; female psychologists</li>
  </ul>

  <div class="cta-band"><span class="phone">Call: 9563 2190</span></div>
  <svg class="cta-arrow" viewBox="0 0 200 126"><polygon points="0,0 150,0 200,63 150,126 0,126" fill="#f7dc55"/></svg>
  <p class="cta-arrow-text">Make your appointment today!</p>

  <div class="clinic-name"><i></i>Brightwater Wellbeing Rooms</div>

  <div class="web-band">brightwaterwellbeingrooms.com.au</div>

  <div class="swatch-strip strip-bottom"><span></span><span></span><span></span><span></span><span></span><span></span><span></span><span></span></div>
</section>

<section class="panel back">
  <div class="faint-ring"></div>

  <h2 class="topic-head head-parenting">PARENTING</h2>
  <p class="topic-text text-parenting">Parenthood is an amazing journey, but for lots of people it raises all sorts of issues from fear of birth, breastfeeding difficulties and settling problems, to toddler discipline and food fussiness all the way through to getting help for your depressed or anxious adolescent. Our Parenting Psychologists can help you be the best parent you can be which will in turn lead to happier families, homes, children and parents.</p>

  <h2 class="topic-head head-chronic">CHRONIC PAIN &amp; ILLNESS</h2>
  <p class="topic-text text-chronic">Diabetes, heart disease, arthritis, asthma, migraines, dizziness, chronic fatigue syndrome, infertility, and PCOS are just some of the conditions that can be managed with psychological interventions. Everything we do is about helping you to manage your condition and get back to focusing on what you really want your life to be about.</p>

  <h2 class="topic-head head-eating">EATING</h2>
  <p class="topic-text text-eating">Whether you suffer from anorexia, bulimia or binge eating, our strategies help you develop a healthy relationship with food and your body. The practical tips and strategies that we can provide are very useful for people undergoing lapband surgery or liposuction.</p>

  <div class="info-band">
    <span class="phone">Call: 9563 2190</span>
    <span class="visit">Or visit: brightwaterwellbeingrooms.com.au</span>
  </div>
  <svg class="info-arrow" viewBox="0 0 160 112"><polygon points="0,0 125,0 160,56 125,112 0,112" fill="#1d7a80"/></svg>
  <p class="info-arrow-text">For<br>more<br>info:</p>

  <p class="address">Suite 1/1287 Marlowe Rd. Kelverton East 3185</p>

  <div class="swatch-strip strip-bottom"><span></span><span></span><span></span><span></span><span></span><span></span><span></span><span></span></div>
</section>

</body>
</html>
```